Business card, Letterhead and envelope design
Create a business card, letterhead and envelope design for Velmira Solutions
Professional
name
title
address
email@velmira-example.com
www.velmirasolutions-example.com
logo and font
Trifold brochure design we have for inspiration of design. This is for reference only.

```html
<!DOCTYPE html>
<html lang="en">
<head>
<meta charset="utf-8">
<title>Velmira Solutions – Stationery Set</title>
<link href="https://fonts.googleapis.com/css2?family=Arimo:wght@400;700&display=swap" rel="stylesheet">
<style>
  :root{
    --page:#ffffff;
    --board:#e6e7e9;
    --navy:#0b2e5a;
    --blue:#1a8fd6;
    --sky:#bfe3f7;
    --ink:#33414f;
    --label:#1a6fb5;
    --card-dark:#0d3a72;
    --shadow:rgba(0,0,0,.18);
  }
  *{margin:0;padding:0;box-sizing:border-box}
  html,body{width:1200px;height:881px;overflow:hidden;background:var(--page);font-family:"Arimo",Arial,sans-serif;color:var(--ink)}
  .board{position:absolute;left:24px;top:84px;width:1092px;height:768px;background:var(--board)}
  .piece{position:absolute;background:#fff;box-shadow:0 1px 4px var(--shadow);overflow:hidden}
  .wave{position:absolute;left:0;top:0;width:100%;display:block}
  .brand{position:absolute;display:flex;align-items:center;gap:10px}
  .brand-mark{background:var(--navy);flex:none}
  .brand-name{font-weight:700;color:var(--navy);line-height:1}
  .brand-name span{display:block}
  .faint-mark{position:absolute;background:var(--navy);opacity:.06}

  /* Letterhead */
  .letterhead{left:43px;top:96px;width:521px;height:763px}
  .letterhead .wave{height:140px}
  .letterhead .brand{left:26px;top:26px}
  .letterhead .brand-mark{width:60px;height:60px}
  .letterhead .brand-name{font-size:30px}
  .letterhead .brand-name span+span{font-size:20px;font-weight:700}
  .letterhead .faint-mark{left:150px;top:330px;width:200px;height:200px}
  .lh-address{position:absolute;left:0;right:0;bottom:30px;text-align:center;font-size:7px}
  .lh-contacts{position:absolute;left:0;right:0;bottom:14px;text-align:center;font-size:7px}
  .lh-contacts b{color:var(--label)}

  /* Business cards */
  .card{width:329px;height:142px}
  .card-light{left:631px;top:115px}
  .card-dark{left:806px;top:281px;width:228px;height:132px;background:var(--card-dark)}
  .card .wave{height:95px}
  .card .brand{left:14px;top:14px;gap:7px}
  .card .brand-mark{width:32px;height:32px}
  .card .brand-name{font-size:17px}
  .card .brand-name span+span{font-size:12px}
  .card-name{position:absolute;font-size:15px;color:var(--label)}
  .card-light .card-name{left:14px;top:108px}
  .card-details{position:absolute;font-size:6px;line-height:1.45}
  .card-details b{color:var(--label)}
  .card-light .card-details{left:128px;top:96px}
  .card-dark .card-name{left:12px;top:88px;color:#fff;font-size:13px}
  .card-dark .card-details{left:100px;top:76px;color:#fff}
  .card-dark .card-details b{color:#8fd0f5}
  .card-dark .brand{left:10px;top:10px}
  .card-dark .brand-mark{width:26px;height:26px}
  .card-dark .brand-name{font-size:14px}
  .card-dark .brand-name span+span{font-size:10px}

  /* Envelope */
  .envelope{left:473px;top:439px;width:585px;height:396px}
  .envelope .wave{height:250px}
  .envelope .brand{left:14px;top:110px;gap:10px}
  .envelope .brand-mark{width:58px;height:58px}
  .envelope .brand-name{font-size:28px}
  .envelope .brand-name span+span{font-size:19px}
  .envelope .seal-mark{position:absolute;left:274px;top:22px;width:34px;height:34px;background:var(--navy)}
  .envelope .faint-mark{left:440px;top:280px;width:100px;height:100px}
  .env-address{position:absolute;left:20px;top:326px;font-size:6.5px;line-height:1.5}
  .env-address b{color:var(--label)}
</style>
</head>
<body>
<svg width="0" height="0" style="position:absolute" aria-hidden="true">
  <defs>
    <linearGradient id="sky" x1="0" y1="0" x2="1" y2="0">
      <stop offset="0" stop-color="#d6eefa"/>
      <stop offset="0.6" stop-color="#8ccaf0"/>
      <stop offset="1" stop-color="#2f97da"/>
    </linearGradient>
    <linearGradient id="sky-env" x1="0" y1="0" x2="0" y2="1">
      <stop offset="0" stop-color="#9fd5f4"/>
      <stop offset="1" stop-color="#e3f3fc"/>
    </linearGradient>
    <linearGradient id="sky-dark" x1="0" y1="0" x2="1" y2="0">
      <stop offset="0" stop-color="#1f67b0"/>
      <stop offset="1" stop-color="#5fb7ea"/>
    </linearGradient>
  </defs>
</svg>

<div class="board"></div>

<section class="piece letterhead" aria-label="Letterhead">
  <svg class="wave" viewBox="0 0 500 130" preserveAspectRatio="none" aria-hidden="true">
    <rect width="500" height="110" fill="url(#sky)"/>
    <path d="M0 84 C150 58 300 112 500 44 L500 52 C300 120 150 66 0 92Z" fill="#1a8fd6"/>
    <path d="M0 92 C150 66 300 124 500 56 L500 66 C300 132 150 76 0 100Z" fill="#0b2e5a"/>
    <path d="M0 100 C150 76 300 132 500 66 L500 130 L0 130Z" fill="#fff"/>
  </svg>
  <div class="brand">
    <div class="brand-mark"></div>
    <div class="brand-name"><span>Velmira</span><span>Solutions</span></div>
  </div>
  <div class="faint-mark"></div>
  <p class="lh-address">36 Harbor Lane, Suite 4, Brookfield, ON 00000</p>
  <p class="lh-contacts"><b>Office:</b> 555 010 2471 &nbsp;|&nbsp; <b>Fax:</b> 555 010 2472 &nbsp;|&nbsp; <b>Email:</b> email@velmira-example.com &nbsp;|&nbsp; <b>Web:</b> www.velmirasolutions-example.com</p>
</section>

<section class="piece card card-light" aria-label="Business card, front">
  <svg class="wave" viewBox="0 0 500 130" preserveAspectRatio="none" aria-hidden="true">
    <rect width="500" height="110" fill="url(#sky)"/>
    <path d="M0 84 C150 58 300 112 500 44 L500 52 C300 120 150 66 0 92Z" fill="#1a8fd6"/>
    <path d="M0 92 C150 66 300 124 500 56 L500 66 C300 132 150 76 0 100Z" fill="#0b2e5a"/>
    <path d="M0 100 C150 76 300 132 500 66 L500 130 L0 130Z" fill="#fff"/>
  </svg>
  <div class="brand">
    <div class="brand-mark"></div>
    <div class="brand-name"><span>Velmira</span><span>Solutions</span></div>
  </div>
  <p class="card-name">Adrian Kole</p>
  <p class="card-details">36 Harbor Lane, Brookfield, ON 00000<br>
    <b>Office:</b> 555 010 2471<br>
    <b>Fax:</b> 555 010 2472<br>
    <b>Email:</b> email@velmira-example.com<br>
    <b>Web:</b> www.velmirasolutions-example.com</p>
</section>

<section class="piece card card-dark" aria-label="Business card, back">
  <svg class="wave" viewBox="0 0 500 130" preserveAspectRatio="none" aria-hidden="true" style="height:80px">
    <rect width="500" height="110" fill="url(#sky-dark)"/>
    <path d="M0 84 C150 58 300 112 500 44 L500 52 C300 120 150 66 0 92Z" fill="#8fd0f5"/>
    <path d="M0 92 C150 66 300 124 500 56 L500 130 L0 130Z" fill="#0d3a72"/>
  </svg>
  <div class="brand">
    <div class="brand-mark" style="background:#fff"></div>
    <div class="brand-name" style="color:#fff"><span>Velmira</span><span>Solutions</span></div>
  </div>
  <p class="card-name">Adrian Kole</p>
  <p class="card-details">36 Harbor Lane, Brookfield<br>
    <b>Office:</b> 555 010 2471<br>
    <b>Fax:</b> 555 010 2472<br>
    <b>Email:</b> email@velmira-example.com<br>
    <b>Web:</b> www.velmirasolutions-example.com</p>
</section>

<section class="piece envelope" aria-label="Envelope">
  <svg class="wave" viewBox="0 0 585 250" preserveAspectRatio="none" aria-hidden="true">
    <rect width="585" height="230" fill="url(#sky-env)"/>
    <path d="M0 0 L292 110 L585 0" fill="none" stroke="#ffffff" stroke-opacity=".6" stroke-width="1.5"/>
    <path d="M0 170 C180 140 360 215 585 135 L585 146 C360 228 180 154 0 182Z" fill="#1a8fd6"/>
    <path d="M0 182 C180 154 360 228 585 146 L585 160 C360 242 180 168 0 196Z" fill="#0b2e5a"/>
    <path d="M0 196 C180 168 360 242 585 160 L585 250 L0 250Z" fill="#fff"/>
  </svg>
  <div class="seal-mark"></div>
  <div class="brand">
    <div class="brand-mark"></div>
    <div class="brand-name"><span>Velmira</span><span>Solutions</span></div>
  </div>
  <div class="faint-mark"></div>
  <p class="env-address">36 Harbor Lane, Brookfield, ON 00000<br>
    <b>Office:</b> 555 010 2471<br>
    <b>Fax:</b> 555 010 2472<br>
    <b>Email:</b> email@velmira-example.com<br>
    <b>Web:</b> www.velmirasolutions-example.com</p>
</section>
</body>
</html>
```